Wealth management podcast „Kolem krbu”

I need a podcast cover (square) and episode banner (rectangle) for wealth management (investment advisory) podcast called „Kolem krbu”. This stands for „Around the hearth”.

Cover should be logo and the two gentlemen.
Banner should be logo, two gentlemen and episode number & title.

A wealthy man is not a pensioner but a 50-year-old successful business owner.
The name expresses an invitation to a discussion between successful business owners - it is not a battle between two rivals, but a joint discussion in a group.
Visually, we want to evoke prestige, class, wealth.

The cover and episode banner should serve to build trust and promote Radek Horvatek (main), Miroslav Kubelka.
Photo Miroslav: https://www.filevaultsample.net/s/qa7wm3kd9ty2rb4/KUBELKA_01.jpg?dl=0
Photo Radek: https://www.filevaultsample.net/s/hn4vp8sj2lc6xe1/KUBELKA_06.jpg?dl=0

Target Market(s)

50-year-old successful business owner

Industry/Entity Type

Wealth management, financial advisory

Font styles to use
Sans Serif

Requirements
Must have
• cover & episode banner
Nice to have
• Logo,

```html
<!DOCTYPE html>
<html lang="cs">
<head>
<meta charset="utf-8">
<title>Kolem krbu – podcast cover</title>
<link rel="stylesheet" href="https://fonts.googleapis.com/css2?family=Jost:wght@500;600;700&family=Poppins:wght@600;700&display=swap">
<style>
  :root {
    --charcoal: #2a2a2a;
    --charcoal-soft: #333333;
    --orange: #f08c1a;
    --white: #ffffff;
    --bar-grey: #7a7a7a;
    --photo-light: #bdbdbd;
    --photo-dark: #3a3a3a;
  }
  html, body {
    margin: 0;
    padding: 0;
    width: 1200px;
    height: 1200px;
    overflow: hidden;
    background: var(--charcoal);
  }
  .cover {
    position: relative;
    width: 1200px;
    height: 1200px;
    overflow: hidden;
    background: var(--charcoal);
  }
  .cover-art {
    position: absolute;
    inset: 0;
  }
  .hosts-names {
    position: absolute;
    left: 130px;
    top: 184px;
    margin: 0;
    font-family: "Jost", sans-serif;
    font-weight: 600;
    font-size: 64px;
    line-height: 71px;
    color: var(--white);
    letter-spacing: 1px;
  }
  .hosts-names .amp { color: var(--charcoal); }
  .show-title {
    position: absolute;
    left: 100px;
    top: 620px;
    margin: 0;
    line-height: 1;
  }
  .show-title .line-one {
    display: block;
    font-family: "Jost", sans-serif;
    font-weight: 700;
    font-size: 212px;
    color: var(--white);
    letter-spacing: 2px;
    height: 185px;
  }
  .show-title .line-two {
    display: block;
    font-family: "Poppins", sans-serif;
    font-weight: 600;
    font-size: 206px;
    color: var(--orange);
    letter-spacing: 1px;
    margin-top: -10px;
  }
  .episode {
    position: absolute;
    left: 99px;
    top: 1016px;
    width: 1014px;
    height: 90px;
  }
  .episode-number {
    position: absolute;
    left: 0;
    top: 0;
    width: 91px;
    height: 90px;
    border-radius: 14px;
    background: var(--orange);
    color: var(--white);
    font-family: "Poppins", sans-serif;
    font-weight: 700;
    font-size: 38px;
    display: flex;
    align-items: center;
    justify-content: center;
    box-shadow: 0 4px 8px rgba(0,0,0,0.35);
  }
  .episode-bar {
    position: absolute;
    left: 95px;
    top: 0;
    right: 0;
    height: 90px;
    border-radius: 14px;
    background: var(--bar-grey);
    box-shadow: 0 4px 8px rgba(0,0,0,0.35);
    display: flex;
    align-items: center;
    padding-left: 48px;
    box-sizing: border-box;
  }
  .episode-lead {
    font-family: "Poppins", sans-serif;
    font-weight: 700;
    font-size: 74px;
    color: var(--white);
    line-height: 1;
    margin-top: 6px;
  }
  .episode-topic {
    margin-left: 22px;
    font-family: "Poppins", sans-serif;
    font-weight: 600;
    font-size: 29px;
    line-height: 31px;
    color: var(--white);
    text-transform: uppercase;
  }
</style>
</head>
<body>
<main class="cover">
  <svg class="cover-art" width="1200" height="1200" viewBox="0 0 1200 1200" xmlns="http://www.w3.org/2000/svg">
    <defs>
      <linearGradient id="deskFade" x1="0" y1="0" x2="1" y2="1">
        <stop offset="0" stop-color="#383838"/>
        <stop offset="1" stop-color="#2a2a2a"/>
      </linearGradient>
      <linearGradient id="portraitTone" x1="0" y1="0" x2="0" y2="1">
        <stop offset="0" stop-color="var(--photo-light)"/>
        <stop offset="0.55" stop-color="#8a8a8a"/>
        <stop offset="1" stop-color="var(--photo-dark)"/>
      </linearGradient>
      <clipPath id="aboveWave">
        <path d="M0,0 H1200 V702 C1100,745 960,775 860,765 C760,755 700,700 640,640 C580,580 520,520 350,473 L0,473 Z"/>
      </clipPath>
    </defs>

    <rect class="desk-backdrop" x="0" y="430" width="620" height="770" fill="url(#deskFade)" opacity="0.6" role="img" aria-label="Faint dark photo of a desk with a calculator and coins"/>

    <path class="orange-blob" fill="var(--orange)"
      d="M266,0 H1200 V702 C1100,745 960,775 860,765 C760,755 700,700 640,640 C580,580 520,520 350,473 C200,440 90,380 83,250 C80,130 160,40 266,0 Z"/>

    <g class="host-portraits" clip-path="url(#aboveWave)" role="img" aria-label="Black and white portrait photo of the two hosts, Radek and Miroslav, in dark suits and white shirts">
      <path fill="url(#portraitTone)" d="M350,480 C420,440 470,430 495,400 C480,340 470,290 470,230 C470,120 520,40 595,40 C670,40 715,120 715,230 C715,290 705,340 690,400 C760,430 830,470 870,560 L900,800 L350,800 Z"/>
      <path fill="url(#portraitTone)" d="M770,500 C800,480 830,470 845,450 C825,390 805,330 805,260 C805,150 860,60 920,60 C980,60 1030,150 1030,260 C1030,330 1015,390 1000,450 C1060,470 1120,490 1200,520 L1200,800 L770,800 Z"/>
    </g>

    <path class="wave-line" fill="none" stroke="var(--orange)" stroke-width="3"
      d="M350,473 C520,520 580,580 640,640 C700,700 760,755 860,765 C960,775 1100,745 1200,702"/>
  </svg>

  <p class="hosts-names">RADEK <span class="amp">&amp;</span><br>MIROSLAV</p>

  <h1 class="show-title">
    <span class="line-one">KOLEM</span>
    <span class="line-two">KRBU</span>
  </h1>

  <div class="episode">
    <div class="episode-number">#1</div>
    <div class="episode-bar">
      <span class="episode-lead">HOW TO</span>
      <span class="episode-topic">Protect your wealth even<br>if you don't invest</span>
    </div>
  </div>
</main>
</body>
</html>
```